need label redone so i can edit it, it was ai generated.

Hey, this label design was originally generated by AI, and while I like the overall layout, there are several issues with it. Some elements are not lossless, others appear distorted, uneditable, or low quality.
What I need is a complete recreation of this label—exactly as it is—without adding any new creative touches. Please rebuild every element of the label from scratch, but make sure the final file is in a fully editable, high-resolution format (preferably an .ai file or equivalent).
Each part of the label (text, shapes, background, colors, etc.) should be separated into layers or components so I can easily change anything I want later—like the font, colors, text, or images.
Quality and editability are the top priorities here. Please make sure the design is 100% lossless and flexible for editing.

```html
<!DOCTYPE html>
<html lang="en">
<head>
<meta charset="utf-8">
<title>SurfPup Beach Towel Label</title>
<link rel="stylesheet" href="https://fonts.googleapis.com/css2?family=Poppins:wght@800&family=Oswald:wght@500;600;700&family=Lobster+Two:ital,wght@1,700&display=swap">
<style>
  :root {
    --sky: #86cfd5;
    --sky-light: #92d6db;
    --navy: #054e6f;
    --orange: #e08614;
    --white: #ffffff;
    --yellow: #f5e000;
    --sand: #eed5a3;
    --sand-deep: #e4c183;
    --sea: #3f9fb8;
    --coast: #d9b27a;
  }
  * { margin: 0; padding: 0; box-sizing: border-box; }
  html, body { width: 899px; height: 1200px; overflow: hidden; background: var(--sky); }
  .label { position: relative; width: 899px; height: 1200px; overflow: hidden; background: var(--sky); }
  .layer { position: absolute; left: 0; top: 0; width: 899px; height: 1200px; }

  .brand { position: absolute; top: 58px; left: 168px; display: flex; align-items: center; gap: 18px; }
  .brand-dot { width: 70px; height: 70px; border-radius: 50%; background: var(--navy); }
  .brand-name { font-family: "Poppins", sans-serif; font-weight: 800; font-size: 92px; line-height: 1; color: var(--navy); letter-spacing: 1px; }

  .headline text { font-family: "Poppins", sans-serif; font-weight: 800; fill: var(--white); }
  .tagline-script { font-family: "Lobster Two", cursive; font-style: italic; font-weight: 700; fill: var(--yellow); }
  .pill-text { font-family: "Oswald", sans-serif; font-weight: 600; fill: var(--white); }

  .badge { position: absolute; border-radius: 50%; display: flex; flex-direction: column; align-items: center; justify-content: center; text-align: center; color: var(--white); font-family: "Oswald", sans-serif; font-weight: 600; line-height: 1; }
  .badge-absorbent { left: 94px; top: 677px; width: 160px; height: 178px; background: var(--orange); }
  .badge-absorbent .big { font-family: "Poppins", sans-serif; font-weight: 800; font-size: 68px; line-height: 0.9; letter-spacing: -3px; }
  .badge-absorbent .mid { font-size: 30px; margin-top: 4px; }
  .badge-absorbent .small { font-size: 27px; letter-spacing: -0.5px; }
  .badge-beachbag { left: 251px; top: 805px; width: 155px; height: 170px; background: var(--navy); }
  .badge-beachbag .mid { font-size: 37px; line-height: 1.02; }
  .badge-beachbag .small { font-size: 23px; margin-top: 4px; }
  .badge-car { left: 92px; top: 871px; width: 156px; height: 172px; background: var(--navy); }
  .badge-car .mid { font-size: 31px; line-height: 1.17; }

  .closing { position: absolute; left: 34px; top: 1078px; font-family: "Oswald", sans-serif; font-weight: 700; font-size: 33px; line-height: 56px; color: var(--navy); }

  .features { position: absolute; left: 676px; top: 1116px; display: flex; gap: 6px; }
  .feature { width: 44px; display: flex; flex-direction: column; align-items: center; }
  .feature-icon { width: 34px; height: 34px; border-radius: 50%; border: 2.5px solid var(--navy); background: var(--white); display: flex; align-items: center; justify-content: center; }
  .feature-label { margin-top: 3px; font-family: "Poppins", sans-serif; font-weight: 800; font-size: 7px; line-height: 1.1; color: var(--navy); text-align: center; white-space: nowrap; }
</style>
</head>
<body>
<div class="label">

  <svg class="layer background" viewBox="0 0 899 1200" aria-hidden="true">
    <rect width="899" height="1200" fill="var(--sky)"/>
    <path d="M0 240 C120 220 200 150 330 165 C470 180 560 215 899 170 L899 420 L0 450 Z" fill="var(--sky-light)" opacity="0.55"/>
    <path d="M0 450 C160 440 260 470 380 500 L899 410 L899 700 L0 700 Z" fill="var(--sky)" opacity="0.6"/>
    <path d="M0 845 C120 840 200 850 300 865 L300 1200 L0 1200 Z" fill="var(--sand)"/>
    <path d="M0 845 L899 800 L899 1200 L0 1200 Z" fill="var(--sand)"/>
    <path d="M0 1042 L899 1040 L899 1200 L0 1200 Z" fill="var(--sand-deep)"/>
  </svg>

  <div class="brand">
    <div class="brand-dot"></div>
    <div class="brand-name">SURFPUP</div>
  </div>

  <svg class="layer hero-panel" viewBox="0 0 899 1200" aria-hidden="true">
    <path d="M110 258 C300 250 460 250 700 218 C780 210 820 250 828 300 L818 625 C700 590 560 590 420 622 C300 648 200 665 120 640 C80 625 70 590 70 560 L72 320 C72 280 90 262 110 258 Z" fill="var(--navy)"/>
  </svg>

  <svg class="layer pill" viewBox="0 0 899 1200" aria-hidden="true">
    <g transform="rotate(-6 256 268)">
      <rect x="108" y="213" width="296" height="116" rx="58" fill="var(--orange)"/>
      <text class="pill-text" x="256" y="265" font-size="32" text-anchor="middle" textLength="222" lengthAdjust="spacingAndGlyphs">DRY YOUR DOG</text>
      <text class="pill-text" x="256" y="299" font-size="32" text-anchor="middle" textLength="232" lengthAdjust="spacingAndGlyphs">FASTER THAN EVER!</text>
    </g>
  </svg>

  <svg class="layer headline" viewBox="0 0 899 1200">
    <text x="117" y="440" font-size="128" textLength="652" lengthAdjust="spacingAndGlyphs" transform="rotate(-7 117 440)">DRY YOUR DOG</text>
    <text x="146" y="544" font-size="128" textLength="600" lengthAdjust="spacingAndGlyphs" transform="rotate(-7 146 544)">IN SECONDS</text>
    <text class="tagline-script" x="116" y="605" font-size="50" textLength="672" lengthAdjust="spacingAndGlyphs" transform="rotate(-8 116 605)">The Ultimate Beach Towel for Dogs</text>
  </svg>

  <svg class="layer product-photo" viewBox="0 0 899 1200" role="img" aria-label="Photo: a happy golden retriever wrapped in a teal towel standing on a sandy beach with ocean waves behind">
    <defs>
      <linearGradient id="sceneTone" x1="0" y1="0" x2="0" y2="1">
        <stop offset="0" stop-color="var(--sea)"/>
        <stop offset="0.3" stop-color="#9fcfd6"/>
        <stop offset="0.45" stop-color="var(--coast)"/>
        <stop offset="1" stop-color="#e2b877"/>
      </linearGradient>
    </defs>
    <path d="M179 722 L510 720 C520 640 570 585 640 585 C700 585 740 640 738 715 L817 717 L817 1030 C817 1070 790 1100 740 1102 L300 1102 C240 1070 200 1000 179 960 Z" fill="url(#sceneTone)"/>
  </svg>

  <div class="badge badge-absorbent">
    <span class="big">5x</span>
    <span class="mid">MORE</span>
    <span class="small">ABSORBENT</span>
  </div>
  <div class="badge badge-beachbag">
    <span class="mid">BEACH<br>BAG</span>
    <span class="small">MUST-HAVE</span>
  </div>
  <div class="badge badge-car">
    <span class="mid">NO MORE<br>WET CAR<br>RIDES</span>
  </div>

  <p class="closing">Trade the Stack of<br>towels for One That Works.</p>

  <div class="features">
    <div class="feature">
      <div class="feature-icon">
        <svg width="20" height="14" viewBox="0 0 20 14" aria-hidden="true"><path d="M1 9 C4 5 7 5 10 8 C13 11 16 10 19 6" fill="none" stroke="var(--navy)" stroke-width="3" stroke-linecap="round"/></svg>
      </div>
      <div class="feature-label">MACHINE<br>WASHABLE</div>
    </div>
    <div class="feature">
      <div class="feature-icon">
        <svg width="14" height="18" viewBox="0 0 14 18" aria-hidden="true"><path d="M7 1 C10 6 13 9 13 12 A6 6 0 0 1 1 12 C1 9 4 6 7 1 Z" fill="var(--navy)"/></svg>
      </div>
      <div class="feature-label">FAST<br>DRYING</div>
    </div>
    <div class="feature">
      <div class="feature-icon">
        <svg width="16" height="18" viewBox="0 0 16 18" aria-hidden="true"><path d="M8 17 L8 6 M8 9 C4 9 2 6 2 3 C6 3 8 5 8 9 M8 9 C12 9 14 6 14 3 C10 3 8 5 8 9" fill="none" stroke="var(--navy)" stroke-width="2" stroke-linecap="round"/></svg>
      </div>
      <div class="feature-label">ECO<br>FRIENDLY</div>
    </div>
  </div>

</div>
</body>
</html>
```